Graphic Design/Logo Needed for Ear Drops Bottle

We have an Ear Drop Medication that we need to create a new label for. We will use a retro picture of a Doctor (Dr. Blenham) and the name of the product is Tidy Lobe. There is no official logo, so we will want to create a retro, basic logo for Tidy Lobe and use the retro picture. Front portion of the label is Size is 1.5" in height, and about 1.375" Width. this is a small tube similar in size to eye drops. We will be looking for just the logo portion and what you will see on the front of the bottle.

Target Market(s)

Medical Container

Industry/Entity Type

Medical

Font styles to use
Serif
Sans Serif

Colors
0054AA
0677BA
7BADD7
CADEEF
E8F1F8
FFF300
FFF600
FEFA6F
FFFEC7
FFFEE8

Requirements
Must have
• Picture of Dr. Blenham, "Tidy Lobe", Dr. Blenham's Ear Solution
Nice to have
• Retro Style or Modern with Retro Feel, Clean and engaging

```html
<!DOCTYPE html>
<html lang="en">
<head>
<meta charset="utf-8">
<title>Tidy Lobe – Ear Drops Label</title>
<link rel="stylesheet" href="https://fonts.googleapis.com/css2?family=Poppins:wght@700;800&family=Roboto+Mono:wght@500&display=swap">
<style>
  :root {
    --label-yellow: #FFF600;
    --label-blue: #0677BA;
    --brand-blue: #0054AA;
    --photo-light: #e7dcc2;
    --photo-mid: #c9b890;
    --photo-dark: #8f7a55;
  }
  html, body {
    margin: 0;
    padding: 0;
    width: 1104px;
    height: 1200px;
    overflow: hidden;
    background: #ffffff;
  }
  .label {
    position: relative;
    width: 1104px;
    height: 1200px;
    overflow: hidden;
    background: var(--label-yellow);
  }
  .label__backdrop {
    position: absolute;
    inset: 0;
    width: 1104px;
    height: 1200px;
  }
  .brand {
    position: absolute;
    left: 150px;
    top: 150px;
    display: flex;
    align-items: center;
    gap: 34px;
    transform: rotate(-15deg);
    transform-origin: left center;
  }
  .brand__dot {
    width: 120px;
    height: 120px;
    border-radius: 50%;
    background: var(--brand-blue);
    flex: none;
  }
  .brand__name {
    margin: 0;
    font-family: "Poppins", sans-serif;
    font-weight: 800;
    font-size: 128px;
    line-height: 0.95;
    letter-spacing: 2px;
    color: var(--brand-blue);
    text-transform: uppercase;
  }
  .brand__name span {
    display: block;
  }
  .brand__name .brand__line2 {
    padding-left: 170px;
  }
  .doctor-photo {
    position: absolute;
    left: 540px;
    top: 330px;
    width: 564px;
    height: 870px;
    border-radius: 240px 240px 0 0;
    background: linear-gradient(180deg, var(--photo-light) 0%, var(--photo-mid) 55%, var(--photo-dark) 100%);
  }
  .coat-tag {
    position: absolute;
    right: 40px;
    bottom: 34px;
    margin: 0;
    font-family: "Roboto Mono", monospace;
    font-weight: 500;
    font-size: 22px;
    color: #3a3020;
    letter-spacing: 1px;
  }
</style>
</head>
<body>
  <main class="label">
    <svg class="label__backdrop" viewBox="0 0 414 450" preserveAspectRatio="none" aria-hidden="true">
      <polygon class="corner-accent" points="0,0 42,0 0,18" fill="var(--label-blue)"/>
      <polygon class="top-stripe" points="150,38 300,0 318,0 150,44" fill="var(--label-blue)"/>
      <polygon class="mid-stripe" points="0,270 414,150 414,160 0,282" fill="var(--label-blue)"/>
      <polygon class="lower-band" points="0,302 414,186 414,450 0,450" fill="var(--label-blue)"/>
    </svg>

    <header class="brand">
      <div class="brand__dot"></div>
      <h1 class="brand__name"><span>Tidy</span><span class="brand__line2">Lobe</span></h1>
    </header>

    <div class="doctor-photo" role="img" aria-label="Retro sepia portrait of Dr. Blenham in a white coat with a head mirror">
      <p class="coat-tag">DR. BLENHAM</p>
    </div>
  </main>
</body>
</html>
```